B2B telecom company need web design

We need a web design for our corporate web site. The company exists since almost 10 years.
This is a DESIGN contest, you're expected to provide design only, NOT the whole website. The winner will have to provide the HTML template (with Lorem Ipsum content) and the CSS files of his design.
Our initial product is SMS peering in P2P (you send a SMS to a friend in a foreign country, great chance that your operator route your SMS to us that we route to the recipient). We're launching a bulk SMS service (marketing and application to SMS).
Target is mostly corporate, usually big corporate (operators, contents providers...) where use of SMS is part of the main business.
The web site is composed of 1 landing page and 7 content pages (plan is given for your information, all content page are using the same template and the same design, you do NOT need to make one design per page) :
* About US
Company Profile
They trust us
The Volnor Team
Partners
Contact us
* Solution
P2P SMS
A2P SMS
You only need to submit the landing page and a template page for the content (with h1, h2, h3 and h4).
Design must be based on our new logo (see attached file).
Our current web site http://www.volnor-example.com
The winner of the contest will have to provide state of the art HTML template and CSS files of his design. Photo used shall be downloaded from Pixelbrook (provide the ID of the picture that we purchase file).
Target Market(s)
Telecom operator. SMS Peering hubs. Bulk SMS.
Industry/Entity Type
It Company
Number of Pages Required
2 page

```html
<!DOCTYPE html>
<html lang="en">
<head>
<meta charset="utf-8">
<title>Volnor Mobile</title>
<link rel="stylesheet" href="https://fonts.googleapis.com/css2?family=Lato:wght@400;700;900&display=swap">
<style>
:root{
  --green:#7db52a;
  --green-dark:#6a9c20;
  --ink:#222;
  --text:#555;
  --grey-bg:#f1f1f1;
  --line:#d6d6d6;
  --footer:#333;
  --footer-bottom:#262626;
  --btn-dark:#333;
}
*{box-sizing:border-box;margin:0;padding:0}
html,body{width:761px;height:1200px;overflow:hidden;background:#fff;font-family:'Lato',sans-serif;color:var(--text)}
.page{position:relative;width:761px;height:1200px}
a{color:inherit;text-decoration:none}

.header{position:absolute;top:0;left:0;width:761px;height:61px;background:#fff}
.brand{position:absolute;left:70px;top:18px;font-size:22px;font-weight:400;letter-spacing:1.5px;color:#3a3a3a}
.follow{position:absolute;right:70px;top:13px;display:flex;align-items:center;gap:4px;font-size:10px;color:#444}
.follow span{margin-right:4px}
.sq{display:inline-block;width:17px;height:17px;border-radius:3px}
.sq.a{background:#3aaee2}.sq.b{background:#d8322a}.sq.c{background:#3b5998}
.contacts{position:absolute;right:70px;top:37px;display:flex;gap:20px;font-size:10.5px;color:#333;align-items:center}
.contacts div{display:flex;align-items:center;gap:5px}

.nav{position:absolute;top:61px;left:0;width:761px;height:25px;background:var(--green);display:flex;align-items:center;padding-left:72px;gap:0}
.nav a{color:#fff;font-size:10.5px;margin-right:24px;letter-spacing:.2px}

.hero{position:absolute;top:86px;left:0;width:761px;height:279px;background:radial-gradient(ellipse at 78% 45%,#46536a 0%,#263247 40%,#182336 100%)}
.hero-photo{position:absolute;right:0;top:0;width:400px;height:279px;background:radial-gradient(ellipse at 50% 50%,#4b5566 0%,#313b4c 55%,rgba(30,40,58,0) 100%)}
.hero h1{position:absolute;left:70px;top:76px;font-size:35px;font-weight:700;color:#fff;line-height:1}
.hero h1 em{font-style:normal;color:var(--green)}
.hero h2{position:absolute;left:70px;top:113px;font-size:14.5px;font-weight:700;color:#fff;padding-bottom:4px;border-bottom:1px solid var(--green);width:245px}
.hero p{position:absolute;left:70px;top:145px;width:252px;font-size:9.5px;line-height:11.5px;color:#fff}
.btn-green{display:inline-block;background:var(--green);color:#fff;font-size:9.5px;padding:4px 7px;border-radius:2px}
.hero .btn-green{position:absolute;left:70px;top:187px;padding:5px 7px}

.card{position:absolute;top:403px;width:194px;height:257px;border:1px solid var(--line);background:#fff;text-align:center}
.card .pic{position:absolute;left:4px;top:4px;width:184px;height:124px}
.card .icon{position:absolute;left:72px;top:110px;width:42px;height:42px;border-radius:50%;background:var(--green);border:3px solid #fff;display:flex;align-items:center;justify-content:center}
.card h3{position:absolute;top:161px;left:0;width:100%;font-size:13px;font-weight:700;color:var(--ink)}
.card p{position:absolute;top:181px;left:8px;width:176px;font-size:8.8px;line-height:12px}
.btn-dark{position:absolute;top:220px;left:70px;width:52px;height:18px;line-height:18px;background:var(--btn-dark);color:#fff;font-size:8.5px;font-weight:700;border-radius:2px}

.band{position:absolute;top:705px;left:0;width:761px;height:270px;background:var(--grey-bg)}
.sec-title{position:absolute;font-size:20px;color:var(--ink)}
.arrows{position:absolute;display:flex;gap:2px}
.arrows span{width:10px;height:11px;background:#555;color:#fff;font-size:8px;line-height:11px;text-align:center}
.news{position:absolute;left:70px;width:278px}
.date{position:absolute;left:0;top:0;width:24px;text-align:center}
.date b{display:block;background:var(--green);color:#fff;font-size:12px;line-height:18px}
.date i{display:block;background:#555;color:#fff;font-size:8px;font-style:normal;line-height:11px;font-weight:700}
.news h4{position:absolute;left:34px;top:-2px;font-size:12.5px;font-weight:400;color:var(--ink)}
.news .meta{position:absolute;left:35px;top:17px;font-size:7.5px;color:#444}
.news .meta em{font-style:normal;color:var(--green)}
.news p{position:absolute;left:35px;top:26px;width:245px;font-size:8.8px;line-height:12.6px}
.news .btn-green{position:absolute;left:35px;top:57px;font-size:8.5px}
.divider{position:absolute;left:379px;top:740px;width:1px;height:205px;background:#d8d8d8}
.testi{position:absolute;left:412px;width:278px;height:89px;background:#fff;border:1px solid #e0e0e0}
.testi .q{position:absolute;font-size:22px;font-weight:900;color:var(--green);line-height:1}
.testi p{position:absolute;left:34px;top:9px;width:238px;font-size:8.3px;line-height:12.6px}
.avatar{position:absolute;left:10px;top:51px;width:38px;height:28px;background:linear-gradient(#cfd3d8,#8d949d)}
.testi .who{position:absolute;left:54px;top:50px;font-size:9px;color:var(--ink);line-height:12px}
.testi .who span{display:block;color:#777}

.cta{position:absolute;top:975px;left:0;width:761px;height:59px;background:var(--green);color:#fff}
.cta h5{position:absolute;left:70px;top:20px;font-size:16px;font-weight:700}
.cta .phone{position:absolute;right:70px;top:14px;font-size:25px;display:flex;align-items:center;gap:10px}

.footer{position:absolute;top:1034px;left:0;width:761px;height:131px;background:var(--footer);color:#ccc}
.col{position:absolute;top:15px}
.col h6{font-size:15.5px;font-weight:400;color:#fff;margin-bottom:6px}
.col a{display:block;font-size:8.3px;line-height:12.7px;color:#ccc;padding-left:2px}
.col .row{display:flex;gap:8px;font-size:8.3px;line-height:9px;margin-bottom:8px}
.bottom{position:absolute;top:1165px;left:0;width:761px;height:35px;background:var(--footer-bottom);color:#ddd;font-size:8.5px}
.bottom p{position:absolute;left:70px;top:13px}
.bottom .social{position:absolute;right:70px;top:8px;display:flex;gap:5px}
</style>
</head>
<body>
<div class="page">

<header class="header">
  <div class="brand">VOLNOR mobile</div>
  <div class="follow"><span>Follow Us:</span><i class="sq a"></i><i class="sq b"></i><i class="sq c"></i></div>
  <div class="contacts">
    <div><svg width="13" height="13" viewBox="0 0 24 24"><path fill="#7db52a" d="M6.6 10.8c1.4 2.8 3.8 5.1 6.6 6.6l2.2-2.2c.3-.3.7-.4 1-.2 1.1.4 2.3.6 3.6.6.6 0 1 .4 1 1V20c0 .6-.4 1-1 1C10.6 21 3 13.4 3 4c0-.6.4-1 1-1h3.5c.6 0 1 .4 1 1 0 1.3.2 2.5.6 3.6.1.3 0 .7-.2 1z"/></svg><b style="font-weight:700">+41 22 555 01 23</b></div>
    <div><svg width="16" height="11" viewBox="0 0 16 11"><rect width="16" height="11" fill="#7db52a"/><path d="M0 0l8 6 8-6" stroke="#fff" fill="none"/></svg><span>info@volnor-example.com</span></div>
  </div>
</header>

<nav class="nav">
  <a>HOME</a><a>ABOUT US</a><a>COMPANY PROFILE</a><a>THEY TRUST US</a><a>THE VOLNOR TEAM</a><a>PARTNERS</a><a>CONTACT US</a>
</nav>

<section class="hero">
  <div class="hero-photo" role="img" aria-label="Businessman in a suit tapping a smartphone with message envelopes floating out"></div>
  <h1>VOLNOR <em>Mobile</em></h1>
  <h2>AFRICA &amp; MIDDLE EAST EXCHANGE</h2>
  <p>Lorem ipsum dolor sit amet, consect etur adipiscing elit, sed do eiusmod tempor incididunt ut labore lor em ipsu do con-cestetur.</p>
  <a class="btn-green">Learn More</a>
</section>

<div class="card" style="left:72px">
  <div class="pic" role="img" aria-label="Smiling call centre operator wearing a headset" style="background:linear-gradient(135deg,#d9c3ae,#b8876a 60%,#e8e2dc)"></div>
  <div class="icon"><svg width="20" height="20" viewBox="0 0 24 24" fill="none" stroke="#fff" stroke-width="2"><path d="M4 14v-2a8 8 0 0116 0v2"/><rect x="3" y="13" width="4" height="6" rx="1"/><rect x="17" y="13" width="4" height="6" rx="1"/></svg></div>
  <h3>OPERATOR SERVICES</h3>
  <p>Lorem ipsum dolor sit amet, consect etur adipi scing elit, sed do eiusmod tempor incididunt ut labore lor em ipsu do concestetur.</p>
  <a class="btn-dark">Read More</a>
</div>
<div class="card" style="left:284px">
  <div class="pic" role="img" aria-label="Hands holding a smartphone with message icons floating above" style="background:linear-gradient(135deg,#3a3f46,#6b7078 55%,#2c3036)"></div>
  <div class="icon"><svg width="20" height="16" viewBox="0 0 20 14" fill="none" stroke="#fff" stroke-width="1.6"><rect x="1" y="1" width="18" height="12"/><path d="M1 1l9 7 9-7"/></svg></div>
  <h3>BRAND &amp; CONTENT</h3>
  <p>Lorem ipsum dolor sit amet, consect etur adipi scing elit, sed do eiusmod tempor incididunt ut labore lor em ipsu do concestetur.</p>
  <a class="btn-dark">Read More</a>
</div>
<div class="card" style="left:496px">
  <div class="pic" role="img" aria-label="Young businessman checking his phone in a glass building" style="background:linear-gradient(135deg,#a9c4e4,#6f8fb8 50%,#2d2f38)"></div>
  <div class="icon"><svg width="14" height="22" viewBox="0 0 14 22" fill="none" stroke="#fff" stroke-width="1.8"><rect x="1" y="1" width="12" height="20" rx="2"/><path d="M5 17h4"/></svg></div>
  <h3>ENTERPRISES SERVICES</h3>
  <p>Lorem ipsum dolor sit amet, consect etur adipi scing elit, sed do eiusmod tempor incididunt ut labore lor em ipsu do concestetur.</p>
  <a class="btn-dark">Read More</a>
</div>

<section class="band"></section>
<h2 class="sec-title" style="left:69px;top:725px">Latest News</h2>
<div class="arrows" style="left:326px;top:733px"><span>&lsaquo;</span><span>&rsaquo;</span></div>

<article class="news" style="top:763px;height:90px">
  <div class="date"><b>21</b><i>APR</i></div>
  <h4>Lorem ipsum dolor sit</h4>
  <div class="meta">by <em>Lorem.</em> Mar 16 2015</div>
  <p>Lorem ipsum dolor sit amet, consec tetur adip iscing elit, sed do eiusmod tempor incididuntut labor.Lorem ipsum dolor sit amet,</p>
  <a class="btn-green">Read More</a>
</article>
<div style="position:absolute;left:70px;top:849px;width:278px;height:1px;background:#dcdcdc"></div>
<article class="news" style="top:865px;height:90px">
  <div class="date"><b>21</b><i>APR</i></div>
  <h4>Lorem ipsum dolor sit</h4>
  <div class="meta">by <em>Lorem.</em> Mar 16 2015</div>
  <p>Lorem ipsum dolor sit amet, consec tetur adip iscing elit, sed do eiusmod tempor incididuntut labor.Lorem ipsum dolor sit amet,</p>
  <a class="btn-green">Read More</a>
</article>

<div class="divider"></div>

<h2 class="sec-title" style="left:413px;top:725px">Testimonials</h2>
<div class="arrows" style="left:669px;top:733px"><span>&lsaquo;</span><span>&rsaquo;</span></div>

<div class="testi" style="top:758px">
  <span class="q" style="left:10px;top:8px">&ldquo;</span>
  <p>Lorem ipsum dolor sit amet, consec tetur adip iscing elit, sed do eiusmod tempor incididuntut labor.Lorem ipsum dolor sit amet, tempor incididuntut labor.incididuntut l</p>
  <span class="q" style="left:210px;top:36px">&rdquo;</span>
  <div class="avatar" role="img" aria-label="Client portrait"></div>
  <div class="who">John Doe<span>Lorem Ipsum</span></div>
</div>
<div class="testi" style="top:860px">
  <span class="q" style="left:10px;top:8px">&ldquo;</span>
  <p>Lorem ipsum dolor sit amet, consec tetur adip iscing elit, sed do eiusmod tempor incididuntut labor.Lorem ipsum dolor sit amet, tempor incididuntut labor.incididuntut l</p>
  <span class="q" style="left:210px;top:36px">&rdquo;</span>
  <div class="avatar" role="img" aria-label="Client portrait"></div>
  <div class="who">John Doe<span>Lorem Ipsum</span></div>
</div>

<section class="cta">
  <h5>We're here to help all day, every day.</h5>
  <div class="phone"><svg width="14" height="30" viewBox="0 0 14 30"><path d="M10 2 4 3Q1 15 4 27l6 1 1-6-3-1Q7 15 8 9l3-1z" fill="#fff"/></svg>+41 22 555 01 23</div>
</section>

<footer class="footer">
  <div class="col" style="left:97px"><h6>Company</h6><a>About Us</a><a>The Company Profile</a><a>They Trust Us</a><a>The Volnor Team</a><a>Partners</a><a>Site Map</a></div>
  <div class="col" style="left:244px"><h6>Services</h6><a>Operator Services</a><a>Brand &amp; Content</a><a>Enterprises Services</a></div>
  <div class="col" style="left:366px"><h6>Privacy Policy</h6><a>Privacy Policy</a><a>Legal Use</a><a>Anti-Spam Policy</a></div>
  <div class="col" style="left:530px"><h6>Contact</h6>
    <div class="row" style="margin-top:8px"><svg width="10" height="9" viewBox="0 0 10 9"><path d="M5 0 0 4h1.5v5h7V4H10z" fill="#aaa"/></svg><span>Headquarters (Geneva-<br>Switzerland)<br>Rue des Exemples 12<br>CH-1200 Geneva</span></div>
    <div class="row" style="margin-top:6px"><svg width="10" height="10" viewBox="0 0 24 24"><path fill="#aaa" d="M6.6 10.8c1.4 2.8 3.8 5.1 6.6 6.6l2.2-2.2c.3-.3.7-.4 1-.2 1.1.4 2.3.6 3.6.6.6 0 1 .4 1 1V20c0 .6-.4 1-1 1C10.6 21 3 13.4 3 4c0-.6.4-1 1-1h3.5c.6 0 1 .4 1 1 0 1.3.2 2.5.6 3.6.1.3 0 .7-.2 1z"/></svg><span>+41 22 555 01 23</span></div>
    <div class="row"><svg width="10" height="8" viewBox="0 0 10 8"><rect width="10" height="8" fill="#aaa"/><path d="M0 0l5 4 5-4" stroke="#333" fill="none"/></svg><span>info@volnor-example.com</span></div>
  </div>
</footer>

<div class="bottom">
  <p>Copyright 2015 VOLNOR Mobile Exchange. All Rights reserved</p>
  <div class="social"><i class="sq a"></i><i class="sq b"></i><i class="sq c"></i></div>
</div>

</div>
</body>
</html>
```